Kambo Flyer

to create a Flyer with information about Kambo Ceremonies. The flyer that is up loaded is an example

Requirements
Must have
• Benefits of Kambo
• Kambo is traditionally known to be anti-inflammatory, to relieve joint pain, to heal eyesight, and to ease pain. Kambo peptides, and their effects, are reported to cover a wide range of potential medical uses: treatment of brain diseases such as Alzheimer’s and Parkinson’s, depression, migraines, blood circulation problems, vascular insufficiency, organ diseases, skin and eyes issues, cancer, fertility problems in women, AIDS, candida, hepatitis, herpes, and more
• What is Kambo
• The scientific name for this frog is Phyllomedusa bicolor or “Two-Colored Leaf Guardian.” It is also known as the “Giant Green Monkey Tree Frog.”
• Kambo is legal in the United States, as well as all other countries, and is not a hallucinogenic. It is, however, a deep cleansing therapy – – physically, emotionally and mentally. It is one of the world’s most effective and natural antibiotics and immune system boosters. It detoxifies the liver and intestines, improves mental functioning, and has the potential to dissolve emotional blocks. It also helps to reset our cellular memory.
• Please note that fasting 12 hours prior to the ceremony is required
• Private (in Home} Semi-Private and Group Ceremonies Available
• For More information see our website
• www.MeadowLightHalls.org
• 555-214-0873
• Traditional Shamanic Kambo Ceremonies in Florida

```html
<!DOCTYPE html>
<html lang="en">
<head>
<meta charset="utf-8">
<title>Kambo Ceremonies Flyer</title>
<link rel="stylesheet" href="https://fonts.googleapis.com/css2?family=Bebas+Neue&family=Montserrat:wght@300;500;600;700&family=Roboto:wght@400;500&display=swap">
<style>
:root{
  --green:#31a84b;
  --dark:#262626;
  --light:#f1f1f1;
  --white:#ffffff;
  --text:#333333;
  --title:#111111;
}
*{margin:0;padding:0;box-sizing:border-box}
html,body{width:923px;height:1200px;overflow:hidden;background:var(--light)}
.flyer{position:relative;width:923px;height:1200px;background:var(--light);overflow:hidden;font-family:'Montserrat',sans-serif}
.header-band{position:absolute;left:0;top:0;width:923px;height:340px;background:var(--green)}
.social{position:absolute;left:20px;color:var(--white);font-weight:500;font-size:17px;letter-spacing:.2px;display:flex;align-items:center;gap:14px}
.social .dot{width:16px;height:16px;background:var(--white);border-radius:50%}
.social .square{width:15px;height:15px;background:var(--white)}
.social.first{top:16px}
.social.second{top:49px}
.dates{position:absolute;right:26px;top:10px;color:var(--white);font-size:12.5px;font-weight:600}
.headline{position:absolute;right:58px;top:58px;text-align:right;color:var(--white);font-weight:300;font-size:78px;line-height:60px;letter-spacing:1px}
.headline-rule{position:absolute;left:490px;top:250px;width:375px;height:6px;background:var(--white)}
.availability{position:absolute;right:55px;top:270px;width:420px;text-align:right;color:var(--white);font-family:'Roboto',sans-serif;font-size:15.5px;line-height:22px}
.intro-panel{position:absolute;left:0;top:0;width:923px;height:600px}
.fasting-note{position:absolute;left:20px;top:109px;color:var(--white);font-weight:500;font-size:17.5px;line-height:22px;text-transform:uppercase}
.tagline{position:absolute;left:52px;top:218px;color:#eeeeee;font-family:'Bebas Neue',sans-serif;font-size:62px;line-height:60px;letter-spacing:.5px;font-weight:400}
.cta{position:absolute;left:384px;font-weight:600;font-size:36px;color:var(--white);padding-left:9px;line-height:1}
.cta.line-one{top:364px;width:276px;height:36px;background:var(--green);padding-top:1px}
.cta.line-two{top:402px;width:494px;height:50px;background:var(--dark);padding-top:8px}
.cta.line-three{top:453px;width:388px;height:37px;background:var(--green);padding-top:1px}
.contact{position:absolute;left:386px;top:491px;font-weight:700;font-size:16px;line-height:18px;color:var(--dark)}
.ceremony-photo{position:absolute;left:0;top:543px;width:923px;height:391px;background:linear-gradient(90deg,#3a1a12 0%,#8a3a22 30%,#5a2a18 45%,#0e0e0e 60%,#1d3a14 78%,#0d0d0d 100%)}
.info-icon{position:absolute;display:flex;align-items:center;justify-content:center}
.info-icon.benefits{left:139px;top:902px;width:66px;height:60px;background:var(--dark)}
.info-icon.about{left:433px;top:934px;width:67px;height:63px;background:var(--green)}
.info-icon.legal{left:741px;top:901px;width:68px;height:58px;background:var(--dark)}
.column{position:absolute;text-align:center;font-family:'Roboto',sans-serif;color:var(--text);font-size:13.8px;line-height:17px}
.column h2{font-family:'Roboto',sans-serif;font-weight:500;font-size:17px;color:var(--title);line-height:21px;margin-bottom:1px}
.column.benefits{left:6px;top:963px;width:338px}
.column.about{left:352px;top:1005px;width:244px}
.column.legal{left:598px;top:962px;width:316px}
.footer-band{position:absolute;left:0;top:1171px;width:923px;height:29px;background:var(--green)}
</style>
</head>
<body>
<main class="flyer">
  <div class="header-band"></div>

  <div class="social first"><span class="dot"></span>@MEADOWLIGHTRITES</div>
  <div class="social second"><span class="square"></span>@MEADOWLIGHTCIRCLE</div>
  <div class="dates">08TH / 10TH / 12TH DECEMBER</div>

  <h1 class="headline">WHAT<br>IS<br>KAMBO</h1>
  <div class="headline-rule"></div>
  <p class="availability">Private (in Home} Semi-Private and Group Ceremonies Available</p>

  <div class="ceremony-photo" role="img" aria-label="Photo of a practitioner applying kambo with a wooden stick beside a glowing green tree frog"></div>

  <svg class="intro-panel" width="923" height="600" viewBox="0 0 923 600" aria-hidden="true">
    <polygon points="0,104 449,104 330,573 0,573" fill="#262626"/>
  </svg>
  <p class="fasting-note">Please note that fasting 12 hours<br>prior to the ceremony is required</p>
  <h2 class="tagline">Traditional<br>Shamanic<br>Kambo<br>Ceremonies<br>in Florida</h2>

  <div class="cta line-one">FOR MORE</div>
  <div class="cta line-two">INFORMATION SEE OUR</div>
  <div class="cta line-three">WEBSITE</div>
  <p class="contact">WWW.MEADOWLIGHTHALLS.ORG<br>555-214-0873</p>

  <div class="info-icon benefits">
    <svg width="34" height="34" viewBox="0 0 24 24"><polygon points="12,2 14.9,8.6 22,9.3 16.6,14 18.2,21 12,17.3 5.8,21 7.4,14 2,9.3 9.1,8.6" fill="#ffffff"/></svg>
  </div>
  <div class="info-icon about">
    <svg width="36" height="36" viewBox="0 0 24 24"><circle cx="12" cy="12" r="7.5" fill="none" stroke="#ffffff" stroke-width="3" stroke-dasharray="3 2.9"/><circle cx="12" cy="12" r="5.2" fill="none" stroke="#ffffff" stroke-width="2"/><circle cx="12" cy="12" r="2" fill="#ffffff"/></svg>
  </div>
  <div class="info-icon legal">
    <svg width="32" height="32" viewBox="0 0 24 24"><circle cx="12" cy="8" r="5" fill="#ffffff"/><path d="M2 22c0-5 4.5-8 10-8s10 3 10 8z" fill="#ffffff"/></svg>
  </div>

  <section class="column benefits">
    <h2>BENEFITS OF KAMBO</h2>
    <p>Kambo is traditionally known to be anti-inflammatory, to relieve joint pain, to heal eyesight, and to ease pain. Kambo peptides, and their effects, are reported to cover a wide range of potential medical uses: treatment of brain diseases such as Alzheimer’s and Parkinson’s, depression, migraines, blood circulation problems, vascular insufficiency, organ diseases, skin and eyes issues, cancer, fertility problems in women, AIDS, candida, hepatitis, herpes, and more</p>
  </section>

  <section class="column about">
    <h2>WHAT IS KAMBO</h2>
    <p>The scientific name for this frog is Phyllomedusa bicolor or “Two-Colored Leaf Guardian.” It is also known as the “Giant Green Monkey Tree Frog.”</p>
  </section>

  <section class="column legal">
    <p>Kambo is legal in the United States, as well as all other countries, and is not a hallucinogenic. It is, however, a deep cleansing therapy – – physically, emotionally and mentally. It is one of the world’s most effective and natural antibiotics and immune system boosters. It detoxifies the liver and intestines, improves mental functioning, and has the potential to dissolve emotional blocks. It also helps to reset our cellular memory.</p>
  </section>

  <div class="footer-band"></div>
</main>
</body>
</html>
```